Construction Company

Design a clutter free business card, it can be double-sided utilizing the logo for BDN Ltd simple with all relevant contact information.

Please also a letterhead design to function for the purposes of invoicing, all mail requirements, with header to be distinctive while the footer ties page together and incorporates all necessary information.

For now, please use generic / dummy text and when a winner is selected, I will disclose the contact information.

Hi Designers! Please read the updated brief which includes the design of a business card and letterhead. Thank you!

```html
<!DOCTYPE html>
<html lang="en">
<head>
<meta charset="utf-8">
<title>BDN Ltd – Business Card</title>
<link href="https://fonts.googleapis.com/css2?family=Roboto:wght@400;500&display=swap" rel="stylesheet">
<style>
  :root {
    --backdrop: #d9dadc;
    --card: #2b2b2c;
    --card-edge: #1f4fc1;
    --gold: #d9a92a;
    --blue: #1c44b8;
    --text: #e6e6e6;
    --muted: #9a9a9a;
    --silver: #8c8c8e;
    --rule: #cfcfcf;
  }
  * { box-sizing: border-box; margin: 0; padding: 0; }
  html, body { width: 1200px; height: 834px; overflow: hidden; }
  body {
    background: var(--backdrop);
    font-family: "Roboto", Arial, sans-serif;
    display: flex;
    align-items: center;
    justify-content: center;
    gap: 60px;
  }
  .card {
    position: relative;
    width: 525px;
    height: 300px;
    background: var(--card);
    border-bottom: 3px solid var(--card-edge);
    border-left: 3px solid var(--card-edge);
    box-shadow: 0 12px 30px rgba(0,0,0,0.25);
    color: var(--text);
  }
  /* Front */
  .card-front .identity { position: absolute; left: 34px; top: 40px; }
  .person-name { color: var(--gold); font-size: 24px; font-weight: 500; }
  .person-role { font-size: 15px; margin-top: 4px; }
  .divider {
    position: absolute; left: 34px; right: 34px; top: 112px;
    height: 1px; background: var(--rule);
  }
  .contact-list { position: absolute; left: 34px; top: 132px; list-style: none; }
  .contact-list li {
    display: flex; align-items: center; gap: 10px;
    font-size: 15px; line-height: 26px;
  }
  .contact-list svg { width: 13px; height: 13px; fill: var(--gold); flex: none; }
  .brand-front {
    position: absolute; right: 40px; top: 140px;
    display: flex; align-items: center; gap: 10px;
    color: var(--blue); font-size: 40px; font-weight: 500; letter-spacing: 1px;
  }
  .brand-mark { width: 16px; height: 16px; border-radius: 50%; background: var(--gold); }
  .address {
    position: absolute; right: 34px; bottom: 26px;
    text-align: right; font-size: 15px; line-height: 21px; color: var(--text);
  }
  /* Back */
  .card-back .brand-back {
    position: absolute; left: 0; right: 0; top: 100px;
    text-align: center;
    color: var(--silver); font-size: 54px; font-weight: 500; letter-spacing: 2px;
  }
  .card-back .website {
    position: absolute; left: 0; right: 0; top: 190px;
    text-align: center; font-size: 14px; color: var(--text);
  }
</style>
</head>
<body>
  <section class="card card-front">
    <div class="identity">
      <p class="person-name">Daniel Hart</p>
      <p class="person-role">Manager</p>
    </div>
    <div class="divider"></div>
    <ul class="contact-list">
      <li>
        <svg viewBox="0 0 24 24" aria-hidden="true"><path d="M6.6 10.8a15 15 0 0 0 6.6 6.6l2.2-2.2c.3-.3.7-.4 1-.2 1.1.4 2.3.6 3.6.6.6 0 1 .4 1 1V20c0 .6-.4 1-1 1A17 17 0 0 1 3 4c0-.6.4-1 1-1h3.5c.6 0 1 .4 1 1 0 1.3.2 2.5.6 3.6.1.3 0 .7-.2 1z"/></svg>
        123-555-0148
      </li>
      <li>
        <svg viewBox="0 0 24 24" aria-hidden="true"><path d="M2 5h20v14H2zm2 2v.5l8 5 8-5V7zm0 2.9V17h16V9.9l-8 5z"/></svg>
        hello@bdnltd.com
      </li>
      <li>
        <svg viewBox="0 0 24 24" aria-hidden="true"><path d="M12 2a10 10 0 1 0 0 20 10 10 0 0 0 0-20zm6.9 6h-3a15 15 0 0 0-1.3-3.9A8 8 0 0 1 18.9 8zM12 4c.8 1.2 1.5 2.5 1.9 4h-3.8c.4-1.5 1.1-2.8 1.9-4zM4.3 14a8 8 0 0 1 0-4h3.4a16 16 0 0 0 0 4zm.8 2h3a15 15 0 0 0 1.3 3.9A8 8 0 0 1 5.1 16zm3-8h-3a8 8 0 0 1 4.3-3.9A15 15 0 0 0 8.1 8zM12 20c-.8-1.2-1.5-2.5-1.9-4h3.8c-.4 1.5-1.1 2.8-1.9 4zm2.3-6H9.7a14 14 0 0 1 0-4h4.6a14 14 0 0 1 0 4zm.3 5.9a15 15 0 0 0 1.3-3.9h3a8 8 0 0 1-4.3 3.9zm1.7-5.9a16 16 0 0 0 0-4h3.4a8 8 0 0 1 0 4z"/></svg>
        www.bdnltd.com
      </li>
    </ul>
    <div class="brand-front">
      <span class="brand-mark"></span>
      <span class="brand-name">BDN LTD</span>
    </div>
    <p class="address">Your address here<br>city state zip</p>
  </section>

  <section class="card card-back">
    <p class="brand-back">BDN LTD</p>
    <p class="website">www.bdnltd.com</p>
  </section>
</body>
</html>
```